Swimming Pool Supply Company Business Cards

We need business cards designed for company. These need to be easy to edit so that we can fill in names, titles, and contact info for each person who works here.

Dalton R. Whitfield
Manager of Legal & Finance
K.L. Brisbane, Incorporated

4837 Grenway Avenue
Marlow Heights, PA 19243

E. dalton@klbrisbane-example.com
M. (215) 555-0173
O. (215) 555-0148

Contact Information for Business Card

Looking to upgrade current business cards with graphic that can be edited. Looking for fresh ideas for an age old industry.

Font styles to use
Serif
Sans Serif

Colors

Designer to choose colors to be used in the design.

Requirements
Must have
• Professional, fresh, unique but professional

```html
<!DOCTYPE html>
<html lang="en">
<head>
<meta charset="utf-8">
<title>K.L. Brisbane Business Cards</title>
<link rel="stylesheet" href="https://fonts.googleapis.com/css2?family=Lato:wght@400;700;900&display=swap">
<style>
  :root {
    --backdrop: #1c1c1c;
    --card: #ffffff;
    --ink: #231f20;
    --ink-soft: #3a3a3a;
    --band-dark: #231f20;
    --band-grey: #707070;
  }
  * { margin: 0; padding: 0; box-sizing: border-box; }
  html, body {
    width: 1200px; height: 1200px; overflow: hidden;
    background: var(--backdrop);
    font-family: "Lato", sans-serif;
    color: var(--ink);
  }
  .sheet {
    position: relative; width: 1200px; height: 1200px;
    display: flex; flex-direction: column; align-items: center; justify-content: center; gap: 70px;
  }
  .card {
    position: relative; width: 875px; height: 500px;
    background: var(--card); overflow: hidden;
  }
  .card-shapes { position: absolute; inset: 0; width: 100%; height: 100%; }
  .brand { position: absolute; }
  .brand-name {
    font-weight: 900; letter-spacing: 6px; line-height: 1; color: var(--ink);
  }
  .brand-tagline { font-weight: 700; color: var(--ink); letter-spacing: 0.1px; }

  /* front */
  .card-front .brand { left: 0; right: 0; top: 140px; text-align: center; }
  .card-front .brand-name { font-size: 92px; }
  .card-front .brand-tagline { font-size: 20px; margin-top: 8px; }

  /* back */
  .card-back .brand { left: 34px; top: 36px; }
  .card-back .brand-name { font-size: 64px; letter-spacing: 4px; }
  .card-back .brand-tagline { font-size: 16px; margin-top: 6px; }

  .person { position: absolute; right: 60px; top: 118px; text-align: right; }
  .person-name { font-size: 32px; font-weight: 900; color: var(--ink-soft); }
  .person-role { font-size: 21px; line-height: 1.2; color: var(--ink-soft); margin-top: 4px; }

  .address {
    position: absolute; left: 34px; top: 280px;
    display: flex; gap: 8px; font-size: 22px; line-height: 1.3;
  }
  .address .icon { width: 16px; height: 22px; margin-top: 3px; }

  .contacts {
    position: absolute; right: 40px; top: 286px;
    list-style: none; text-align: right; font-size: 21px;
  }
  .contacts li { display: flex; justify-content: flex-end; align-items: center; gap: 16px; height: 38px; }
  .contacts .icon { width: 20px; height: 20px; flex: none; }
</style>
</head>
<body>
<main class="sheet">

  <section class="card card-front" aria-label="Card front">
    <svg class="card-shapes" viewBox="0 0 875 500" aria-hidden="true">
      <rect x="0" y="462" width="875" height="38" fill="var(--band-grey)"/>
      <path d="M0 425 H520 C565 425 570 500 625 500 H0 Z" fill="var(--band-dark)"/>
      <rect x="-14" y="62" width="30" height="130" rx="12" fill="var(--band-dark)"/>
      <rect x="855" y="290" width="40" height="112" rx="12" fill="var(--band-dark)"/>
    </svg>
    <div class="brand">
      <div class="brand-name">BRISBANE</div>
      <div class="brand-tagline">Big Enough to Serve You, Small Enough to Care</div>
    </div>
  </section>

  <section class="card card-back" aria-label="Card back">
    <svg class="card-shapes" viewBox="0 0 875 500" aria-hidden="true">
      <rect x="0" y="458" width="875" height="42" fill="var(--band-grey)"/>
      <path d="M875 425 H430 C380 425 372 500 318 500 H875 Z" fill="var(--band-dark)"/>
      <rect x="-14" y="14" width="30" height="110" rx="12" fill="var(--band-dark)"/>
      <rect x="855" y="120" width="40" height="120" rx="12" fill="var(--band-dark)"/>
    </svg>

    <div class="brand">
      <div class="brand-name">BRISBANE</div>
      <div class="brand-tagline">Big Enough to Serve You, Small Enough to Care</div>
    </div>

    <div class="person">
      <div class="person-name">Dalton R. Whitfield</div>
      <div class="person-role">Manager of Legal &amp; Finance</div>
      <div class="person-role">K.L. Brisbane, Incorporated</div>
    </div>

    <div class="address">
      <svg class="icon" viewBox="0 0 16 22" aria-hidden="true">
        <path d="M8 1a7 7 0 0 0-7 7c0 5 7 13 7 13s7-8 7-13a7 7 0 0 0-7-7zm0 10a3 3 0 1 1 0-6 3 3 0 0 1 0 6z" fill="var(--ink)"/>
      </svg>
      <div>
        <div>4837 Grenway Avenue</div>
        <div>Marlow Heights, PA 19243</div>
      </div>
    </div>

    <ul class="contacts">
      <li><span>(215) 555-0173</span>
        <svg class="icon" viewBox="0 0 20 20" aria-hidden="true"><rect x="5" y="1" width="10" height="18" rx="2" fill="none" stroke="var(--ink)" stroke-width="1.6"/><line x1="8" y1="16" x2="12" y2="16" stroke="var(--ink)" stroke-width="1.4"/></svg></li>
      <li><span>(215) 555-0148</span>
        <svg class="icon" viewBox="0 0 20 20" aria-hidden="true"><path d="M2 7c0-3 16-3 16 0v2h-4V7H6v2H2z" fill="var(--ink)"/><path d="M5 10h10l2 7H3z" fill="var(--ink)"/><circle cx="10" cy="13.5" r="2" fill="#fff"/></svg></li>
      <li><span>dalton@klbrisbane-example.com</span>
        <svg class="icon" viewBox="0 0 20 20" aria-hidden="true"><rect x="1" y="4" width="18" height="12" fill="var(--ink)"/><path d="M1.5 4.5 L10 11 L18.5 4.5" fill="none" stroke="#fff" stroke-width="1.2"/></svg></li>
    </ul>
  </section>

</main>
</body>
</html>
```